Billboard design for a jewelry store.

I am looking for a very unique design with a catchy slogan, I am looking for billboard so good that will make the front page of the newspaper. I want to target customers that are looking for diamond jewelry or diamonds in general. For sure not interested in anything that is genetic or been used in the past. I want the billboard to stand out and very unique. Text not more than 3 words, our logo and an image.

Target Market(s)

Local

Industry/Entity Type

Jewelry Store

Font styles to use
Other font styles liked:
• Open to your suggestion for the font.

Requirements
Must have
• Unique, very brief a catchy slogan. My logo and an image. Open for suggestions. I want also different formats to use on social media.
Nice to have
• I am open to unique and amazing new ideas. I don't want general used design or slogan.
Should not have
• Too much text

```html
<!DOCTYPE html>
<html lang="en">
<head>
<meta charset="utf-8">
<title>Ravelle Jewelers Billboard</title>
<link rel="stylesheet" href="https://fonts.googleapis.com/css2?family=Cinzel:wght@700&family=Questrial&display=swap">
<style>
  :root {
    --canvas: #ffffff;
    --board-dark: #2b2121;
    --grey-light: #dedddd;
    --grey-mid: #a6a5a5;
    --grey-stripe: #c9c8c8;
    --text-light: #ffffff;
    --photo-light: #d9d9d9;
    --photo-mid: #8a8a8a;
    --photo-dark: #3a3a3a;
  }
  html, body {
    margin: 0;
    padding: 0;
    width: 1200px;
    height: 1200px;
    overflow: hidden;
    background: var(--canvas);
  }
  .stage {
    width: 1200px;
    height: 1200px;
    display: flex;
    align-items: center;
    justify-content: center;
  }
  .billboard {
    width: 1100px;
    height: 299px;
    display: block;
    filter: drop-shadow(0 8px 10px rgba(0, 0, 0, 0.35));
  }
  .brand-name {
    font-family: "Cinzel", serif;
    font-weight: 700;
    fill: var(--text-light);
  }
  .slogan {
    font-family: "Questrial", sans-serif;
    fill: var(--text-light);
  }
</style>
</head>
<body>
<main class="stage">
  <svg class="billboard" viewBox="0 0 1380 375" xmlns="http://www.w3.org/2000/svg">
    <defs>
      <linearGradient id="photoTone" x1="0" y1="0" x2="1" y2="1">
        <stop offset="0" stop-color="var(--photo-light)"/>
        <stop offset="0.5" stop-color="var(--photo-mid)"/>
        <stop offset="1" stop-color="var(--photo-dark)"/>
      </linearGradient>
    </defs>

    <!-- base panel -->
    <rect class="panel-base" x="0" y="0" width="1380" height="375" fill="var(--grey-light)"/>
    <polygon class="corner-wedge" points="0,0 100,0 40,190 0,160" fill="var(--grey-mid)"/>

    <!-- main dark chevron field -->
    <polygon class="panel-field" points="95,0 1380,0 1380,375 115,375 35,195" fill="var(--board-dark)"/>

    <!-- accent stripes -->
    <polygon class="accent-stripe" points="1085,0 1215,0 955,72 905,78" fill="var(--grey-stripe)"/>
    <polygon class="accent-line" points="848,160 856,160 832,375 824,375" fill="var(--grey-mid)"/>

    <!-- photo area -->
    <path class="photo-area" role="img" aria-label="Black and white photo of hands placing a diamond engagement ring on a finger"
          d="M868,375 L868,125 Q868,82 912,76 L1380,14 L1380,375 Z" fill="url(#photoTone)"/>

    <!-- brand name -->
    <text class="brand-name" x="495" y="207" font-size="92" text-anchor="middle" letter-spacing="4">RAVELLE</text>
    <text class="brand-name" x="495" y="247" font-size="30" text-anchor="middle" letter-spacing="16">JEWELERS</text>

    <!-- slogan -->
    <text class="slogan" x="495" y="308" font-size="38" text-anchor="middle">A symbol of Love</text>
  </svg>
</main>
</body>
</html>
```